social interest sharing site needs a web site design

we need a web site design for a social web platform.
the site is one page(main page), that is split into 3 sections
each section is a different color(red,green and blue)
and a user can choose to share each of the sections.
any section/color will contain boxes , each box can contain different media types.

the media types:
* list of URLS
* list of articles including title + image + description
* list of videos
* thumbnails of images
* calender
* list of emails

the main content will look like quiltboard layout
multiple boxes each box can contain different type of content as described above

each color is a different tab
each tab will have layout like quiltboard
Updates

please read the last description update.
and i uploaded an image that can explain the requirements better

thanks
Oren

```html
<!DOCTYPE html>
<html lang="en">
<head>
<meta charset="utf-8">
<title>Hueshare.me — Social Interest</title>
<link href="https://fonts.googleapis.com/css2?family=Open+Sans:wght@400;600;700;800&family=Ubuntu:wght@400;500;700&display=swap" rel="stylesheet">
<style>
:root{
  --white:#ffffff;
  --ink:#222222;
  --muted:#666666;
  --red:#cc0000;
  --red-dark:#b30000;
  --green:#7ea727;
  --green-dark:#6a8f1e;
  --blue:#0683b3;
  --footer:#3a3a3a;
  --footer-text:#d0d0d0;
  --header-bg:rgba(255,255,255,.92);
  --circle-btn:#3b5998;
  --chirp:#2fa7e4;
  --dark-card:#3b3b3b;
  --hero-a:#6d6f68;
  --hero-b:#a69c8c;
  --hero-c:#d8cfc2;
}
*{box-sizing:border-box;margin:0;padding:0}
html,body{width:1200px;height:2403px;overflow:hidden}
body{font-family:"Open Sans",Arial,sans-serif;color:var(--ink);position:relative;background:var(--white)}
a{color:inherit;text-decoration:none}

/* header */
.site-header{position:absolute;top:0;left:0;width:1200px;height:75px;background:var(--header-bg);z-index:5}
.brand{position:absolute;left:102px;top:16px;display:flex;align-items:center;gap:10px;font-family:"Ubuntu",sans-serif;font-weight:700;font-size:31px;color:var(--red)}
.brand-dot{width:34px;height:34px;border-radius:50%;background:var(--red)}
.auth{position:absolute;top:21px;left:555px;display:flex;gap:7px;align-items:center}
.auth-btn{height:29px;display:flex;align-items:center;gap:10px;padding:0 12px;color:var(--white);font-size:12px;font-weight:600}
.auth-btn .mark{width:14px;height:14px;background:rgba(255,255,255,.85)}
.auth-circle{background:var(--circle-btn);width:186px}
.auth-chirp{background:var(--chirp);width:185px}
.auth-signup{background:#111;width:74px;justify-content:center;margin-left:2px}
.auth-login{font-size:13px;font-weight:600;margin-left:16px;color:#111}

/* hero */
.hero{position:absolute;top:0;left:0;width:1200px;height:822px}
.hero-photo{position:absolute;inset:0;background:linear-gradient(90deg,var(--hero-a) 0%,var(--hero-b) 50%,var(--hero-c) 100%)}
.hero-title{position:absolute;left:100px;top:288px;font-weight:800;font-size:60px;letter-spacing:2px;color:var(--white);text-shadow:0 3px 6px rgba(0,0,0,.5)}
.hero-text{position:absolute;left:100px;top:388px;width:540px;font-size:13px;line-height:24px;color:var(--white)}
.hero-actions{position:absolute;left:100px;top:536px;display:flex;gap:15px}
.btn{height:37px;width:142px;display:flex;align-items:center;justify-content:center;font-size:16px;color:var(--white)}
.btn-book{background:var(--red)}
.btn-more{border:2px solid var(--white)}
.scroll-down{position:absolute;left:578px;top:757px;width:44px;height:44px}

/* section shared */
.section{position:absolute;left:0;width:1200px}
.chevron{position:absolute;left:570px;width:60px;height:16px}

/* media types */
.media-types{top:822px;height:528px;background:var(--red);color:var(--white)}
.section-title{position:absolute;top:44px;width:100%;text-align:center;font-family:"Ubuntu",sans-serif;font-weight:700;font-size:27px}
.media-type{position:absolute;top:152px;width:320px;text-align:center}
.media-type svg{height:50px}
.media-type h3{font-family:"Ubuntu",sans-serif;font-weight:700;font-size:25px;margin-top:20px}
.media-type p{font-size:13px;line-height:23.5px;margin:30px auto 0;width:310px}

/* quilt */
.quilt{top:1350px;height:596px;background:var(--green)}
.card{position:absolute;background:var(--white);overflow:hidden}
.card-photo{width:100%}
.card-title{font-size:20px;font-weight:400;text-align:center;margin-top:8px}
.card-text{font-size:10.5px;line-height:17px;color:var(--muted);padding:0 8px;margin-top:10px}
.read-more{display:block;font-size:11px;color:var(--red);font-weight:600;padding:0 8px;margin-top:6px}
.card-meta{position:absolute;bottom:0;left:0;right:0;height:22px;border-top:1px solid #e3e3e3;font-size:10px;color:var(--muted);display:flex;align-items:center;gap:8px;padding-left:6px;background:var(--white)}
.meta-icon{width:14px;height:10px;background:#cfcfcf}
.mini-card{position:absolute;height:117px;display:flex;gap:9px;padding:7px;color:var(--white);border:2px solid rgba(0,0,0,.3)}
.mini-dark{background:var(--dark-card)}
.mini-red{background:var(--red)}
.mini-photo{width:118px;height:99px;flex:none}
.mini-card h4{font-size:17px;font-weight:700;line-height:22px}
.mini-card p{font-size:8.5px;font-weight:700;line-height:14px;margin-top:3px;white-space:nowrap}
.mini-card span{display:block;font-size:9px;margin-top:8px}
.feature{left:422px;top:92px;width:310px;height:451px;border-top:4px solid var(--red)}
.feature .card-photo{position:absolute;top:0;left:0;height:206px}
.feature-badge{position:absolute;left:137px;top:188px;width:36px;height:36px;border-radius:50%;background:var(--red-dark);border:3px solid var(--white)}
.feature h3{position:absolute;top:236px;left:0;width:100%;font-size:18px;font-weight:600;text-align:center;line-height:24px}
.feature .sub{position:absolute;top:294px;left:0;width:100%;font-size:10px;color:#999;text-align:center}
.feature .card-text{position:absolute;top:318px;left:15px;width:280px;text-align:center;padding:0;line-height:19px;margin:0;font-size:11px}
.feature .btn-small{position:absolute;top:402px;left:125px;width:60px;height:20px;background:#333;color:var(--white);font-size:9.5px;line-height:20px;text-align:center;border-radius:2px}
.scrollbar{position:absolute;left:1077px;top:102px;width:10px;height:441px;border:2px solid var(--green-dark);border-radius:5px}
.scrollbar i{position:absolute;left:0;top:0;width:6px;height:26px;background:var(--red);border-radius:3px}

/* info */
.info{top:1946px;height:370px;background:var(--blue);color:var(--white)}
.info-col{position:absolute;top:124px;text-align:center}
.info-col svg{height:22px;display:block;margin:0 auto}
.info-brand{left:97px;width:300px;top:118px}
.info-brand h2{font-family:"Ubuntu",sans-serif;font-weight:500;font-size:29px}
.info-brand p{font-size:13px;line-height:21px;margin-top:16px}
.info-brand .legal{font-size:11px;font-weight:700;margin-top:12px}
.info-col h3{font-family:"Ubuntu",sans-serif;font-weight:400;font-size:17px;margin-top:20px}
.info-col .list{font-size:11px;font-weight:700;line-height:19px;margin-top:16px}
.info-col .plain{font-size:12px;line-height:20px;margin-top:20px;white-space:nowrap}
.footer{position:absolute;top:2316px;left:0;width:1200px;height:87px;background:var(--footer);color:var(--footer-text)}
.footer p{position:absolute;left:102px;top:34px;font-size:14px}
.footer-social{position:absolute;left:950px;top:24px;display:flex;gap:14px}
.footer-social span{width:40px;height:40px;border-radius:50%;background:#555;display:flex;align-items:center;justify-content:center}
</style>
</head>
<body>

<header class="site-header">
  <a class="brand" href="#"><span class="brand-dot"></span>Hueshare.me</a>
  <nav class="auth">
    <a class="auth-btn auth-circle" href="#"><span class="mark"></span>Login with Circlebook</a>
    <a class="auth-btn auth-chirp" href="#"><span class="mark"></span>Login with Chirpline</a>
    <a class="auth-btn auth-signup" href="#">Sign Up</a>
    <a class="auth-login" href="#">Log in</a>
  </nav>
</header>

<section class="hero">
  <div class="hero-photo" role="img" aria-label="Young woman sitting cross-legged with a laptop in a bright blurred hallway"></div>
  <h1 class="hero-title">SOCIAL INTEREST</h1>
  <p class="hero-text">Lorem Ipsum is simply dummy text of the printing and typesetting industry. Lorem Ipsum has been the industry's standard dummy text ever since the 1500s, when an unknown printer took a galley of type and scrambled it to make a type specimen book. It has survived not only five centuries, but also the leap into electronic typesetting, remaining essentially unchanged.</p>
  <div class="hero-actions">
    <a class="btn btn-book" href="#">BOOK NOW</a>
    <a class="btn btn-more" href="#">READ MORE</a>
  </div>
  <svg class="scroll-down" viewBox="0 0 44 44"><circle cx="22" cy="22" r="20" fill="none" stroke="#fff" stroke-width="2"/><path d="M13 17h18l-9 12z" fill="#fff"/></svg>
</section>

<section class="section media-types">
  <h2 class="section-title">THE MEDIA TYPES</h2>
  <div class="media-type" style="left:86px">
    <svg viewBox="0 0 50 50"><g fill="none" stroke="#111" stroke-width="5" stroke-linecap="round"><path d="M22 28l-8 8a6 6 0 0 1-8-8l8-8a6 6 0 0 1 8 0"/><path d="M28 22l8-8a6 6 0 0 1 8 8l-8 8a6 6 0 0 1-8 0"/><path d="M20 30l10-10"/></g></svg>
    <h3>LIST OF URLS</h3>
    <p>Lorem Ipsum is simply dummy text of the printing<br>and typesetting industry. Lorem Ipsum has<br>been the industry's standard dummy<br>text of the printing and<br>setting industry.</p>
  </div>
  <div class="media-type" style="left:432px">
    <svg viewBox="0 0 70 44"><rect width="70" height="44" fill="#111"/><path d="M0 0l35 26 35-26" fill="none" stroke="#cc0000" stroke-width="3"/></svg>
    <h3>LIST OF EMAILS</h3>
    <p>Lorem Ipsum is simply dummy text of the printing<br>and typesetting industry. Lorem Ipsum has<br>been the industry's standard dummy<br>text of the printing and<br>setting industry.</p>
  </div>
  <div class="media-type" style="left:784px">
    <svg viewBox="0 0 50 50"><rect x="3" y="8" width="44" height="40" rx="3" fill="none" stroke="#111" stroke-width="4"/><rect x="3" y="8" width="44" height="9" fill="#111"/><rect x="13" y="2" width="4" height="11" fill="#111"/><rect x="33" y="2" width="4" height="11" fill="#111"/><text x="25" y="43" font-family="Ubuntu,sans-serif" font-weight="700" font-size="22" text-anchor="middle" fill="#111">7</text></svg>
    <h3>CALENDER</h3>
    <p>Lorem Ipsum is simply dummy text of the printing<br>and typesetting industry. Lorem Ipsum has<br>been the industry's standard dummy<br>text of the printing and<br>setting industry.</p>
  </div>
</section>

<section class="section quilt">
  <svg class="chevron" style="top:24px" viewBox="0 0 60 16"><path d="M1 2l29 12 29-12" fill="none" stroke="#222" stroke-width="2"/></svg>

  <article class="card" style="left:100px;top:92px;width:272px;height:313px">
    <div class="card-photo" role="img" aria-label="Group of friends laughing together" style="height:148px;background:linear-gradient(135deg,#c9a27c,#e8c9a8 60%,#d24a4a)"></div>
    <h3 class="card-title">Lorem ipsum</h3>
    <p class="card-text">Lorem Ipsum is simply dummy text of the printing and typesetting industry. Lorem Ipsum has been the are industry's standard dummy text of the printing and setting industry.</p>
    <a class="read-more" href="#">Read More</a>
    <div class="card-meta"><span class="meta-icon"></span>170 Shares &nbsp;- &nbsp;23 minutes ago</div>
  </article>
  <article class="mini-card mini-dark" style="left:99px;top:425px;width:274px">
    <div class="mini-photo" role="img" aria-label="Friends at a party" style="background:linear-gradient(135deg,#6b4a2e,#c99a6a)"></div>
    <div><h4>Lorem ipsum</h4><p>Lorem Ipsum is simply dummy<br>text of the printing and<br>type setting industry.</p><span>Read More</span></div>
  </article>

  <article class="card feature">
    <div class="card-photo" role="img" aria-label="Woman relaxing on a sofa with a laptop" style="background:linear-gradient(135deg,#d9d4cf,#f2efea 55%,#c4a98a)"></div>
    <span class="feature-badge"></span>
    <h3>Lorem Ipsum dolor sit amet<br>consectetur adipscing elit</h3>
    <p class="sub">Lorem ipsum dolor sit</p>
    <p class="card-text">Lorem ipsum dolor sit amet, consectetur adipisicing elit, sed do eiusmod tempo r incididunt ut labore et dolore magna aliqua. Ut enim ad minim veniam, quis consequat.</p>
    <a class="btn-small" href="#">Read More</a>
    <div class="card-meta"><span class="meta-icon" style="width:10px;border-radius:50%"></span>2013/01/05 &nbsp; <span class="meta-icon" style="width:10px"></span>8<span style="margin-left:auto;margin-right:10px;color:#333">★</span></div>
  </article>

  <article class="card" style="left:782px;top:92px;width:272px;height:313px">
    <div class="card-photo" role="img" aria-label="Two students lying on grass with a laptop" style="height:148px;background:linear-gradient(135deg,#5f8f3a,#a9c77a 55%,#d9cdb8)"></div>
    <h3 class="card-title">Lorem ipsum</h3>
    <p class="card-text">Lorem Ipsum is simply dummy text of the printing and typesetting industry. Lorem Ipsum has been the are industry's standard dummy text of the printing and setting industry.</p>
    <a class="read-more" href="#">Read More</a>
    <div class="card-meta"><span class="meta-icon"></span>15 Shares &nbsp;- &nbsp;1 minutes ago</div>
  </article>
  <article class="mini-card mini-red" style="left:781px;top:425px;width:274px">
    <div class="mini-photo" role="img" aria-label="Hand holding a smartphone" style="background:linear-gradient(135deg,#e9ded2,#c8b09a)"></div>
    <div><h4>Lorem ipsum</h4><p>Lorem Ipsum is simply dummy<br>text of the printing and<br>type setting industry.</p><span>Read More</span></div>
  </article>

  <div class="scrollbar"><i></i></div>
</section>

<section class="section info">
  <svg class="chevron" style="top:23px" viewBox="0 0 60 16"><path d="M1 2l29 12 29-12" fill="none" stroke="#222" stroke-width="2"/></svg>
  <div class="info-col info-brand">
    <h2>Hueshare.me</h2>
    <p>Lorem ipsum dolor sit amet, consectetur adipisicing sed do eiusmod tempo r incididunt ut labore et dolore magna aliqua. Ut enim ad minim veniam quis consequat.</p>
    <p class="legal">Terms — Privacy</p>
  </div>
  <div class="info-col" style="left:475px;width:160px">
    <svg viewBox="0 0 34 18"><rect x="1" y="2" width="28" height="14" rx="2" fill="none" stroke="#fff" stroke-width="2"/><rect x="30" y="6" width="3" height="6" fill="#fff"/><rect x="4" y="5" width="12" height="8" fill="#fff"/></svg>
    <h3>Want more?</h3>
    <p class="list">Courses<br>Custom Training<br>Word<br>Layout Loft</p>
  </div>
  <div class="info-col" style="left:663px;width:220px">
    <svg viewBox="0 0 34 26"><path d="M4 9h6l12-7v22l-12-7H4z" fill="#fff"/><path d="M8 17l3 8h4l-2-8" fill="#fff"/><path d="M26 13h6M25 6l5-3M25 20l5 3" stroke="#fff" stroke-width="2"/></svg>
    <h3>Talk to us</h3>
    <p class="plain">Tweet us @hueshare<br><br>Email us hello@hueshare.me</p>
  </div>
  <div class="info-col" style="left:892px;width:240px">
    <svg viewBox="0 0 34 26"><path d="M33 1L1 12l10 4 3 9 5-6 8 5z" fill="#fff"/><path d="M11 16l22-15-14 18" fill="none" stroke="#0683b3" stroke-width="1.5"/></svg>
    <h3>Stay in touch</h3>
    <p class="plain" style="font-size:14px">Get monthly updates from<br>Pinnly in your inbox.</p>
  </div>
</section>

<footer class="footer">
  <p>© 1998–2013 &nbsp;Hueshare.me, All rights reserved.</p>
  <div class="footer-social">
    <span aria-label="Chirpline"></span>
    <span aria-label="Circlebook"></span>
    <span aria-label="Email"><svg width="18" height="13" viewBox="0 0 18 13"><rect width="18" height="13" rx="1" fill="#3a3a3a"/><path d="M1 1l8 6 8-6" fill="none" stroke="#555" stroke-width="1.5"/></svg></span>
  </div>
</footer>

</body>
</html>
```